Delivery Docket urgent plus require many other designs for more stationary after this.

We need a new delivery docket design urgently as the one we have needs updating and we have changed our company name. Please do not copy the one I have uploaded as we do not feel this looks professional enough. I uploaded it as a few designers requested to see what we are currently using thank you.
It is quite complex in that we need a range of information to be on the one docket.
We are a Transport Company based in Australia that has a wide variety of items that we deliver such as water, sand and gravels and heavy equipment transport.
We would prefer to keep this design to A5 size as we will get them made into books. We are looking for a modern professional look. Although it is only a delivery docket this is given to all our customers so needs to look impressive.

We need our new logo on the docket (RWT). There will also need to be areas for our address and contact numbers, email etc these will be supplied to the winning designer to make the final adjustments so for now just put something generic in these spaces.
Needs to have an area for customer details, purchase order number, date and docket number (docket number to be in red)
Needs a section where we can list the type of product / and or service that has been provided and the amount / qty usually 3 lines will be enough for this. Need area under this where the customer can sign name and print name to say that the goods / and or services have been received.

Also required somewhere on the docket are the words, Tax Invoice will be issued based on the information provided on this docket. Conditions on back of page

We then need a separate section on the same page which we will use internally that the staff member can tear off and hand into the office. On this section it needs to have area where the driver can list km at start of job and at end with space to calculate km travelled, details of fuel purchased eg amount and litres, vehicle that is being used. also need to log down wheel bearing temps.
prime mover needs spaces as follows
Steer axel FL____________ Steer axel FR _________ 1st drive axel L_______
1st drive axel R_________ 2nd drive axel L_______ 2nd drive axel R________

For the trailers need something similar x 2 as have 2 trailers
1st axel DS_________ 1st axel PS_________ 2nd axel DS__________
2nd axel PS_________ 3rd axel DS_________ 3rd axel PS__________

I have included a few examples of designs we have used in past and ones that we like so you can get an idea of the colours we prefer, I have included some of the designs we are currently receiving for our logo that I like so you can get idea again of colours we prefer. There is much more we need designed also such as time sheets, more delivery dockets and letter heads so there is a lot of more work available to the winning designer.

Thank you

Target Market(s)

Customers

Font styles to use
Serif
Sans Serif

Colors

Designer to choose colors to be used in the design.

Requirements
Should not have
• Please don't copy old docket as we do not like it and nned new info on new design thank you

```html
<!DOCTYPE html>
<html lang="en">
<head>
<meta charset="utf-8">
<title>RWT Delivery Docket</title>
<link href="https://fonts.googleapis.com/css2?family=Libre+Caslon+Text&family=Open+Sans:wght@400;600;700&display=swap" rel="stylesheet">
<style>
:root{
  --canvas:#e4e4e4;
  --paper:#f7f7f7;
  --ink:#2a2a2a;
  --muted:#555555;
  --navy:#1f2330;
  --black:#111111;
  --rule:#6d6d6d;
  --grid:#9a9a9a;
  --band-grey:#c9c9c9;
  --band-grey-2:#a9a9a9;
  --red:#e0262b;
}
*{box-sizing:border-box;margin:0;padding:0}
html,body{width:941px;height:1200px;overflow:hidden;background:var(--canvas)}
body{position:relative;font-family:"Open Sans",Arial,sans-serif;color:var(--ink)}
.page{position:absolute;top:286px;width:405px;height:578px;background:var(--paper);overflow:hidden;transform:scale(1.0864);transform-origin:0 0;box-shadow:0 2px 6px rgba(0,0,0,.18)}
.page--front{left:20px}
.page--back{left:481px}
.page__photo{position:absolute;left:0;right:0;top:150px;height:390px;background:linear-gradient(180deg,rgba(235,235,235,0) 0%,#e6e6e6 40%,#dedede 70%,rgba(240,240,240,0) 100%)}
.title{position:absolute;left:20px;top:22px;width:195px;text-align:center;font-family:"Libre Caslon Text",Georgia,serif;font-weight:400;font-size:31px;line-height:32px;color:var(--black)}
.docket-no{position:absolute;left:20px;top:90px;width:195px;text-align:center;font-size:11px;letter-spacing:3px;color:var(--red)}
.docket-no span{border-bottom:1px solid var(--red)}
.company{position:absolute;left:20px;top:106px;width:195px;text-align:center;font-size:5.6px;line-height:7.5px;color:var(--muted)}
.brand{position:absolute;left:231px;top:0;width:139px;height:125px;background:radial-gradient(circle at 50% 40%,#4a4a4a 0%,#262626 55%,#141414 100%);display:flex;align-items:center;justify-content:center}
.brand__name{font-family:"Open Sans",Arial,sans-serif;font-weight:700;font-size:34px;letter-spacing:2px;color:#d9d9d9}
.billing{position:absolute;left:231px;top:125px;width:139px;height:51px;background:#e3e3e3;padding:9px 6px 0}
.field{display:flex;align-items:flex-end;font-size:7.2px;line-height:9px;white-space:nowrap;margin-bottom:4px}
.field::after{content:"";flex:1;border-bottom:.7px solid var(--rule);margin-left:3px;margin-bottom:1px}
.field-row{display:flex;gap:14px}
.field-row .field{flex:1}
.customer{position:absolute;left:37px;top:126px;width:185px}
.customer .field-row{gap:4px}
.customer__label{font-size:8px;font-weight:700;margin-bottom:1px}
.goods{position:absolute;left:32px;top:176px;width:338px;border-collapse:collapse;font-size:7.2px}
.goods th{background:var(--navy);color:#fff;font-weight:700;height:20px}
.goods td{height:26.8px;border:.7px solid var(--grid)}
.goods .col-qty{width:57px}
.goods .col-amount{width:84px}
.notice{position:absolute;left:32px;top:410px;width:338px;height:51px;border:.7px solid var(--grid);border-top:none;text-align:center;font-size:7.2px;line-height:12px;padding-top:11px}
.signoff{position:absolute;left:37px;top:504px;width:333px;display:flex;gap:10px}
.signoff .field{flex:1}
.band{position:absolute;left:0;bottom:0;width:405px;height:37px}
.section-head{position:absolute;left:18px;width:368px;height:20px;background:linear-gradient(90deg,#1a1a1a 0%,#262626 60%,#3a3a3a 100%);color:#fff;font-size:10px;font-weight:400;line-height:20px;padding-left:14px;white-space:nowrap}
.log{position:absolute;left:32px;width:340px}
.log .field{margin-bottom:12px;font-size:7.4px}
.log .gap{height:13px}
</style>
</head>
<body>

<section class="page page--front" aria-label="Delivery docket front">
  <div class="page__photo" role="img" aria-label="Faint grey photograph of a heavy haulage truck in the background"></div>
  <h1 class="title">Delivery<br>Docket</h1>
  <p class="docket-no"><span>2050</span></p>
  <p class="company">12 Sample Road, Anytown QLD 4000<br>Ph 07 0000 0000 · office@rwt-transport.example</p>
  <div class="brand"><span class="brand__name">RWT</span></div>

  <div class="customer">
    <p class="customer__label">Customer Details:</p>
    <p class="field">Name:</p>
    <p class="field">Purchase Order Number:</p>
    <div class="field-row">
      <p class="field">Date:</p>
      <p class="field">Phone:</p>
    </div>
  </div>

  <div class="billing">
    <p class="field">Billing Address:</p>
    <p class="field" style="margin-top:6px">&nbsp;</p>
    <p class="field">Contact:</p>
  </div>

  <table class="goods">
    <thead><tr><th class="col-qty">Qty</th><th>Description</th><th class="col-amount">Amount</th></tr></thead>
    <tbody>
      <tr><td></td><td></td><td></td></tr>
      <tr><td></td><td></td><td></td></tr>
      <tr><td></td><td></td><td></td></tr>
      <tr><td></td><td></td><td></td></tr>
      <tr><td></td><td></td><td></td></tr>
      <tr><td></td><td></td><td></td></tr>
      <tr><td></td><td></td><td></td></tr>
      <tr><td></td><td></td><td></td></tr>
    </tbody>
  </table>
  <p class="notice">Tax Invoice will be issued based on the information provided on this docket.<br>Conditions on back of page</p>

  <div class="signoff">
    <p class="field">Print Name</p>
    <p class="field">Sign Name</p>
  </div>

  <svg class="band" viewBox="0 0 405 37" aria-hidden="true">
    <rect x="0" y="0" width="405" height="37" fill="var(--black)"/>
    <polygon points="115,7 260,7 290,37 145,37" fill="var(--band-grey-2)"/>
    <polygon points="175,7 265,7 295,37 205,37" fill="var(--band-grey)"/>
  </svg>
</section>

<section class="page page--back" aria-label="Delivery docket back, driver log">
  <div class="page__photo" role="img" aria-label="Faint grey photograph of a prime mover truck in the background"></div>

  <h2 class="section-head" style="top:36px">Prime Mover Needs Spaces As Follows:</h2>
  <div class="log" style="top:66px">
    <p class="field">Steer axel FL</p>
    <p class="field">Steer axel FR</p>
    <p class="field">1st drive axel L</p>
    <div class="gap"></div>
    <p class="field">1st drive axel R</p>
    <p class="field">2nd drive axel L</p>
    <p class="field">2nd drive axel R</p>
  </div>

  <h2 class="section-head" style="top:216px">For The Trailers Need Something Similar X 2 As Have 2 Trailers:</h2>
  <div class="log" style="top:246px">
    <p class="field">1st axel DS</p>
    <p class="field">1st axel PS</p>
    <p class="field">2nd axel DS</p>
    <div class="gap"></div>
    <p class="field">2nd axel PS</p>
    <p class="field">3rd axel DS</p>
    <p class="field">3rd axel PS</p>
  </div>

  <h2 class="section-head" style="top:396px">Driver Job Details:</h2>
  <div class="log" style="top:426px">
    <div class="field-row">
      <p class="field">Vehicle used</p>
      <p class="field">Km travelled</p>
    </div>
    <div class="field-row">
      <p class="field">Km at start</p>
      <p class="field">Km at end</p>
    </div>
    <div class="field-row">
      <p class="field">Fuel litres</p>
      <p class="field">Fuel amount $</p>
    </div>
  </div>

  <svg class="band" viewBox="0 0 405 37" aria-hidden="true">
    <polygon points="225,0 405,0 405,37 195,37" fill="var(--black)"/>
    <polygon points="145,7 240,7 210,37 115,37" fill="var(--band-grey)"/>
    <polygon points="205,7 260,7 230,37 175,37" fill="var(--band-grey-2)"/>
  </svg>
</section>

</body>
</html>
```